BRIMLOW Pizza and Wraps

We need a website for a new restaurant called BRIMLOW "PIZZA AND WRAPS".
I have attached fonts, background images, logo, images, content etc.
can provide you with what you need to get the website design done fast and easy

I have uploaded more images of the venue and some menu items. let me know if there is anything I need to provide to make your mission clear and easy

Reason: i would like a little time to provide more feedback to designers

Industry/Entity Type

Restaurant

Coding

Coded - Design and coding required

Number of Pages Required

5+ page

Colors

Designer to choose colors to be used in the design.

Requirements
Must have
• PAGES:
• Our Story
• Menu
• Reservations
• Catering & Delivery
• Contact

```html
<!DOCTYPE html>
<html lang="en">
<head>
<meta charset="utf-8">
<title>BRIMLOW Pizza and Wraps</title>
<link href="https://fonts.googleapis.com/css2?family=Arvo:wght@400;700&family=Lato:wght@400;700;900&display=swap" rel="stylesheet">
<style>
:root{
  --red:#e8202a;
  --red-dark:#c4141d;
  --yellow:#ffe600;
  --gold:#f5c400;
  --ink:#222;
  --footer:#231f20;
  --footer-line:#5a5556;
  --white:#fff;
}
*{margin:0;padding:0;box-sizing:border-box}
html,body{width:1200px;height:3495px;overflow:hidden}
body{font-family:'Lato',sans-serif;color:var(--ink);background:var(--white);position:relative;font-size:14px}

/* top bar */
.topbar{position:absolute;top:0;left:0;width:1200px;height:23px;background:var(--gold);display:flex;align-items:center;justify-content:space-between;padding:0 93px}
.topbar .phone{display:flex;align-items:center;gap:8px;font-size:12px;font-weight:700}
.topbar .social{display:flex;gap:14px}
.topbar .social span{width:10px;height:10px;border-radius:50%;background:var(--ink)}

/* header */
.header{position:absolute;top:23px;left:0;width:1200px;height:117px;background:var(--white)}
.brand{position:absolute;left:93px;top:38px;font-family:'Arvo',serif;font-weight:700;font-size:46px;color:var(--red);letter-spacing:1px;line-height:1}
.nav{position:absolute;top:140px;left:0;width:1200px;height:35px;background:var(--red);border-bottom:2px solid var(--red-dark)}
.nav ul{list-style:none;display:flex;position:absolute;left:93px;top:0;height:35px}
.nav li{font-family:'Arvo',serif;font-size:14px;color:var(--white);height:35px;line-height:35px;text-align:center;border-right:1px solid rgba(255,255,255,.45)}
.nav li:last-child{border-right:none}
.nav li.active{background:var(--gold);color:var(--ink)}

/* hero */
.hero{position:absolute;top:175px;left:0;width:1200px;height:424px;background:radial-gradient(ellipse at 55% 40%,#e4cdb2 0%,#b0523a 35%,#5e6a2a 70%,#2d3a17 100%)}
.hero-text{position:absolute;top:130px;left:0;width:1200px;text-align:center}
.hero h1{font-family:'Arvo',serif;font-weight:400;font-size:84px;color:var(--red);line-height:1;letter-spacing:1px;-webkit-text-stroke:2px var(--white);paint-order:stroke fill}
.hero .sub1{font-family:'Arvo',serif;font-size:42px;color:var(--white);margin-top:6px;letter-spacing:1px}
.hero .sub2{font-family:'Arvo',serif;font-size:25px;color:var(--white);letter-spacing:3px;margin-top:2px}
.hero .arrow{position:absolute;top:200px}
.hero .dots{position:absolute;top:376px;left:561px;display:flex;gap:9px}
.hero .dots span{width:12px;height:12px;border-radius:50%;background:var(--gold);opacity:.6}
.hero .dots span.on{opacity:1}

/* section titles */
.section-title{font-family:'Arvo',serif;font-weight:400;font-size:34px;color:var(--red);text-align:center;letter-spacing:1px}
.flourish{width:70px;height:14px;border-radius:7px}

/* story */
.story{position:absolute;top:599px;left:0;width:1200px;height:759px;background:linear-gradient(#fafafa,#e6e6e6)}
.story .section-title{position:absolute;top:34px;width:100%}
.story .flourish{position:absolute;top:88px;left:565px;background:#333}
.story .photo{position:absolute;top:147px;left:102px;width:1016px;height:321px;background:linear-gradient(90deg,#b0533a 0%,#3c2e22 20%,#7a5230 50%,#2a221c 75%,#b5402f 100%)}
.story .copy{position:absolute;top:512px;left:150px;width:900px;text-align:center;font-size:13.5px;line-height:1.55}
.story .copy p{margin-bottom:12px}
.btn{display:inline-block;background:var(--red);color:var(--white);border-radius:20px;font-size:13px;text-align:center}
.story .btn{position:absolute;top:676px;left:538px;width:133px;height:37px;line-height:37px}

/* menu */
.menu{position:absolute;top:1358px;left:0;width:1200px;height:494px;background:var(--yellow)}
.menu .section-title{position:absolute;top:40px;width:100%}
.menu .flourish{position:absolute;top:92px;left:565px;background:var(--red)}
.dish{position:absolute;top:173px;width:322px;text-align:center}
.dish .frame{height:228px;border:4px solid var(--white);box-shadow:0 2px 6px rgba(0,0,0,.35);position:relative}
.dish .name{position:absolute;bottom:14px;left:0;width:100%;color:var(--white);font-weight:700;font-size:27px;text-shadow:0 1px 3px rgba(0,0,0,.6)}
.dish .price{font-weight:700;font-size:16px;margin-top:14px}

/* reservation */
.reservation{position:absolute;top:1852px;left:0;width:1200px;height:380px;background:linear-gradient(90deg,#2b2b2b,#4a4744 50%,#2c2a28)}
.reservation .section-title{position:absolute;top:70px;width:100%;color:var(--white)}
.reservation .flourish{position:absolute;top:124px;left:565px;background:var(--gold)}
.reservation .copy{position:absolute;top:192px;left:200px;width:800px;text-align:center;color:var(--white);font-size:14px;line-height:1.45}
.reservation .copy p{margin-bottom:14px}

/* catering */
.catering{position:absolute;top:2232px;left:0;width:1200px;height:455px;background:var(--white)}
.catering h2{position:absolute;top:92px;left:168px;font-family:'Arvo',serif;font-weight:400;font-size:38px;color:var(--red)}
.catering h2 span{color:var(--ink)}
.catering .copy{position:absolute;top:176px;left:168px;width:508px;font-size:13.5px;line-height:1.5}
.catering .copy p{margin-bottom:16px}
.catering .photo{position:absolute;top:56px;left:734px;width:305px;height:326px;background:linear-gradient(160deg,#d89a30 0%,#6a3a28 40%,#2a2320 75%,#8a8580 100%)}

/* map */
.map{position:absolute;top:2687px;left:0;width:1200px;height:431px;background:linear-gradient(90deg,#dbe5c9,#ecece4 50%,#dde6cf)}

/* footer */
.footer{position:absolute;top:3134px;left:0;width:1200px;height:333px;background:var(--footer);color:var(--white)}
.footer .f-brand{position:absolute;top:80px;left:86px;font-family:'Arvo',serif;font-weight:700;font-size:44px;color:var(--red);line-height:1}
.footer .about{position:absolute;top:168px;left:70px;width:265px;text-align:center;font-size:13.5px;line-height:1.5}
.footer .divider{position:absolute;top:75px;width:1px;height:195px;background:var(--footer-line)}
.footer h3{position:absolute;top:74px;font-family:'Arvo',serif;font-weight:400;font-size:18px;color:var(--red);letter-spacing:.5px}
.footer .links{position:absolute;top:117px;left:401px;list-style:none;font-size:14px;line-height:26px}
.footer .links li::before{content:"‹";margin-right:10px}
.footer .address{position:absolute;top:117px;left:652px;font-size:15px;line-height:26px}
.footer .f-social{position:absolute;top:218px;left:652px;display:flex;gap:18px}
.footer .f-social span{width:11px;height:11px;border-radius:50%;background:#8a8586}
.footer .hours{position:absolute;top:114px;left:905px;width:250px;text-align:center;font-size:12.5px;line-height:16px}
.footer .hours .label{color:var(--gold)}
.footer .btn{position:absolute;top:180px;left:942px;width:144px;height:26px;line-height:26px;border-radius:4px;font-size:12.5px}
.copyright{position:absolute;top:3467px;left:0;width:1200px;height:28px;background:var(--red);color:var(--white);font-size:10px;text-align:center;line-height:28px}
</style>
</head>
<body>

<div class="topbar">
  <div class="phone">
    <svg width="12" height="12" viewBox="0 0 24 24"><path fill="#222" d="M6.6 10.8a15 15 0 0 0 6.6 6.6l2.2-2.2a1 1 0 0 1 1-.25 11.4 11.4 0 0 0 3.6.57 1 1 0 0 1 1 1V20a1 1 0 0 1-1 1A17 17 0 0 1 3 4a1 1 0 0 1 1-1h3.5a1 1 0 0 1 1 1c0 1.25.2 2.45.57 3.57a1 1 0 0 1-.25 1z"/></svg>
    <span>(555) 014 2290</span>
  </div>
  <div class="social"><span></span><span></span><span></span><span></span></div>
</div>

<header class="header">
  <div class="brand">BRIMLOW</div>
</header>

<nav class="nav">
  <ul>
    <li class="active" style="width:93px">Home</li>
    <li style="width:115px">Our Story</li>
    <li style="width:99px">Menu</li>
    <li style="width:148px">Reservations</li>
    <li style="width:180px">Catering&amp;Delivery</li>
    <li style="width:153px">Contact Us</li>
    <li style="width:145px">BookOnline</li>
  </ul>
</nav>

<section class="hero" role="img" aria-label="Close-up photo of a fresh salad with shaved cheese and crispy bacon">
  <svg class="arrow" style="left:22px" width="16" height="26" viewBox="0 0 16 26"><path d="M13 2 3 13l10 11" fill="none" stroke="#fff" stroke-width="3"/></svg>
  <svg class="arrow" style="right:22px" width="16" height="26" viewBox="0 0 16 26"><path d="M3 2l10 11L3 24" fill="none" stroke="#fff" stroke-width="3"/></svg>
  <div class="hero-text">
    <h1>RICH IN HERITAGE</h1>
    <div class="sub1">BRIMLOW IS A GATHERING PLACE</div>
    <div class="sub2">CELEBRATING THE MEDITERRANEAN'S FINEST PRODUCE.</div>
  </div>
  <div class="dots"><span></span><span class="on"></span><span class="on"></span><span></span></div>
</section>

<section class="story">
  <h2 class="section-title">OUR STORY</h2>
  <div class="flourish" role="img" aria-label="Decorative flourish"></div>
  <div class="photo" role="img" aria-label="Photo of the restaurant entrance with brick walls and windows"></div>
  <div class="copy">
    <p>Rich in heritage, Brimlow is a gathering place celebrating the Mediterranean's finest Produce.</p>
    <p>Brimlow is the ultimate escape – the perfect spot to enjoy sensational food and drinks that showcases everything the Mediterranean has to offer in a single, sophisticated setting.</p>
    <p>Where an early morning walk to the bakery around the corner is a way of life, nothing beats the first batch of bread from the oven to start your day. So we combined a variety of best ingredients and delicacies for you to enjoy that experiencewhenever you got the urge to do so</p>
  </div>
  <span class="btn">Read More</span>
</section>

<section class="menu">
  <h2 class="section-title">OUR MENU</h2>
  <div class="flourish" role="img" aria-label="Decorative flourish"></div>
  <div class="dish" style="left:114px">
    <div class="frame" role="img" aria-label="Photo of grilled halloumi" style="background:linear-gradient(160deg,#f3d9a0,#d9a055 55%,#8a5a2a)"><div class="name">Halloumi</div></div>
    <div class="price">$18.00</div>
  </div>
  <div class="dish" style="left:452px">
    <div class="frame" role="img" aria-label="Photo of hummus with olive oil" style="background:radial-gradient(circle at 50% 45%,#e0b84a,#e8c88a 45%,#b7683a 100%)"><div class="name">Hummus</div></div>
    <div class="price">$20.00</div>
  </div>
  <div class="dish" style="left:792px">
    <div class="frame" role="img" aria-label="Photo of a pizza with pepperoni" style="background:linear-gradient(160deg,#d9752a,#b0351d 50%,#6b2a12)"><div class="name">Pizza</div></div>
    <div class="price">$25.00</div>
  </div>
</section>

<section class="reservation" role="img" aria-label="Dim photo of the restaurant dining room">
  <h2 class="section-title">RESERVATION</h2>
  <div class="flourish"></div>
  <div class="copy">
    <p>Tables will only be held for 15 minutes past the reservation time. We appreciate your punctuality.</p>
    <p>Group bookings: All tables of 10 or more guests will have a minimum order requirement of $15 per seat.<br>Please call to make a group booking.</p>
  </div>
</section>

<section class="catering">
  <h2>CATERING <span>&amp;</span> DELIVERY</h2>
  <div class="copy">
    <p>Rich in heritage, Brimlow is a gathering place celebrating the Mediterranean's finest Produce.</p>
    <p>Brimlow is the ultimate escape – the perfect spot to enjoy sensational food and drinks that showcases everything the Mediterranean has to offer in a single, sophisticated setting.</p>
    <p>Where an early morning walk to the bakery around the corner is a way of life, nothing beats the first batch of bread from the oven to start your day. So we combined a variety of best ingredients and delicacies for you to enjoy that experiencewhenever you got the urge to do so</p>
  </div>
  <div class="photo" role="img" aria-label="Photo of the counter with cups and colourful wall art"></div>
</section>

<section class="map" role="img" aria-label="Map showing the restaurant location"></section>

<footer class="footer">
  <div class="f-brand">BRIMLOW</div>
  <p class="about">Rich in heritage, Brimlow is a gathering place celebrating the Mediterranean's finest Produce.</p>
  <div class="divider" style="left:363px"></div>
  <div class="divider" style="left:617px"></div>
  <div class="divider" style="left:876px"></div>
  <h3 style="left:401px">QUICK LINKS</h3>
  <ul class="links">
    <li>Home</li><li>Our Story</li><li>Menu</li><li>Reservations</li><li>Catering&amp;Delivery</li>
  </ul>
  <h3 style="left:652px">CONTACT</h3>
  <div class="address">2418 Alder Park Ave.<br>Suite 140<br>Fresno, CA 93721</div>
  <div class="f-social"><span></span><span></span><span></span><span></span></div>
  <h3 style="left:930px">OPENING HOURS</h3>
  <div class="hours"><div class="label">Opening Hours</div>Daily from: 8am – 10pm<br>Friday: Closed from Noon – 2pm</div>
  <span class="btn">Make a reservation</span>
</footer>
<div class="copyright">© 2017 Brimlowpizza.wraps | Privacy Policy | User Agreement</div>

</body>
</html>
```